Business Card- Can you make it cool vs boring!

Need a refresh on my business card! Want it to be modern but simple, classic and a pop of coolness! we do senior living and it is boring. but that doesn't mean our business card have to look boring! Open to two sided cards. our website is www.Bruvel-HQ.com

Target Market(s)

capital market

Industry/Entity Type

senior housing/ real estate

Contact Information for Business Card

logo/ name/ cell/ address/ www.Bruvel-HQ.com/ space for a QR code

Requirements
Must have
• maybe a QR code (do not make prominent I may not use the QR so design where it can be taken out) that link to more about us/ landing page. needs to be modern but clean
Should not have
• clip art or script

```html
<!DOCTYPE html>
<html lang="en">
<head>
<meta charset="utf-8">
<title>Bruvel Living – Business Cards</title>
<link rel="stylesheet" href="https://fonts.googleapis.com/css2?family=Tinos:wght@400;700&display=swap">
<style>
  :root {
    --backdrop: #eadccb;
    --card-white: #f7f6f4;
    --terracotta: #b8563a;
    --terracotta-deep: #9c3a24;
    --terracotta-light: #c2623f;
    --ink: #2a2220;
    --paper-text: #fbf3ee;
  }
  html, body {
    margin: 0;
    width: 1200px;
    height: 1200px;
    overflow: hidden;
    background: var(--backdrop);
  }
  .canvas {
    position: relative;
    width: 1200px;
    height: 1200px;
  }
  .card {
    position: absolute;
    top: 348px;
    width: 372px;
    height: 565px;
    box-shadow: 0 6px 18px rgba(80, 50, 30, 0.18);
  }
  .card--front { left: 150px; }
  .card--back { left: 678px; }
  .card svg { display: block; }
  .brand-name {
    font-family: "Tinos", "Times New Roman", serif;
    font-size: 38px;
    fill: var(--terracotta);
  }
  .tagline {
    font-family: "Tinos", "Times New Roman", serif;
    font-size: 27px;
    fill: var(--paper-text);
  }
  .person-name {
    font-family: "Tinos", "Times New Roman", serif;
    font-size: 25px;
    fill: var(--ink);
  }
  .person-name .first { font-weight: 700; }
  .person-role {
    font-family: "Tinos", "Times New Roman", serif;
    font-size: 19px;
    fill: var(--ink);
  }
  .contact-line {
    font-family: "Tinos", "Times New Roman", serif;
    font-size: 15px;
    fill: var(--paper-text);
  }
  .icon { fill: none; stroke: var(--paper-text); stroke-width: 1.6; }
  .icon-solid { fill: var(--paper-text); }
</style>
</head>
<body>
<main class="canvas">

  <!-- Front side -->
  <section class="card card--front">
    <svg width="372" height="565" viewBox="0 0 372 565">
      <defs>
        <linearGradient id="front-band" x1="0" y1="1" x2="1" y2="0">
          <stop offset="0" stop-color="var(--terracotta)"/>
          <stop offset="1" stop-color="var(--terracotta-light)"/>
        </linearGradient>
      </defs>
      <rect class="card-face" width="372" height="565" fill="var(--card-white)"/>
      <path class="color-band" d="M0,312 Q186,212 372,312 L372,565 L0,565 Z" fill="url(#front-band)"/>
      <text class="brand-name" transform="translate(205 245) rotate(-90)">Bruvel Living</text>
      <text class="tagline" transform="translate(168 547) rotate(-90)">ASSISTED LIVING</text>
      <text class="tagline" transform="translate(208 547) rotate(-90)">AND MEMORY CARE</text>
    </svg>
  </section>

  <!-- Back side -->
  <section class="card card--back">
    <svg width="372" height="565" viewBox="0 0 372 565">
      <defs>
        <linearGradient id="back-band" x1="0" y1="1" x2="1" y2="0">
          <stop offset="0" stop-color="var(--terracotta)"/>
          <stop offset="1" stop-color="var(--terracotta-deep)"/>
        </linearGradient>
      </defs>
      <rect class="card-face" width="372" height="565" fill="var(--card-white)"/>
      <path class="color-band" d="M0,312 Q186,212 372,312 L372,565 L0,565 Z" fill="url(#back-band)"/>
      <text class="brand-name" transform="translate(205 245) rotate(-90)">Bruvel Living</text>

      <text class="person-name" transform="translate(100 532) rotate(-90)"><tspan class="first">Marlo</tspan> Venden</text>
      <text class="person-role" transform="translate(124 532) rotate(-90)">Manger</text>

      <text class="contact-line" transform="translate(215 500) rotate(-90)">1234 1234 123</text>
      <text class="contact-line" transform="translate(241 500) rotate(-90)">www.Bruvel-HQ.com</text>
      <text class="contact-line" transform="translate(268 500) rotate(-90)">Your Address,country,</text>
      <text class="contact-line" transform="translate(294 500) rotate(-90)">PO,1234</text>

      <!-- phone icon -->
      <g class="icon-phone" transform="translate(210 523) rotate(-90)">
        <path class="icon" d="M-5,-6 q-3,6 2,11 q5,4 9,1 l-2,-3 q-2,1 -4,-1 q-2,-2 -1,-4 z"/>
      </g>
      <!-- globe icon -->
      <g class="icon-globe" transform="translate(252 523)">
        <circle class="icon" r="7"/>
        <ellipse class="icon" rx="3" ry="7"/>
        <line class="icon" x1="-7" y1="0" x2="7" y2="0"/>
      </g>
      <!-- home icon -->
      <g class="icon-home" transform="translate(290 523) rotate(-90)">
        <path class="icon-solid" d="M0,-8 L8,0 L5,0 L5,7 L-5,7 L-5,0 L-8,0 Z"/>
      </g>
    </svg>
  </section>

</main>
</body>
</html>
```